Travel Company is looking for a STAND OUT Business Card

I need a unique Business Card that will truly stand out. Nothing too busy. Simple is good, right? Not looking for a standard design either. No cookie cutter layout. We are a Travel Company that works more with Companies than Travelers. I had an idea to focus and emphasis on the 2 logo a bit more. This is not necessary, however thought it would look interesting. I am just looking for something interesting and a bit different. Does't have to completely off the wall crazy, just not your run of the mill business card.

Target Market(s)

Hoteliers, Resort Management, Call Centers, Executives, Travelers, Families, Businesses

Industry/Entity Type

Hospitality

Contact Information for Business Card

President/CEO - Marco T Villena (title not necessary if design doesn't allow for it)
contact - (407) 555-0182
email - mvillena@roam4ward.example
address - 4127 Brindle Oak Way #164
Orlando, FL 32899
website - www.roam4ward.example

Font styles to use
Serif
Other font styles liked:
• Avenir Next LT Pro BOLD

Requirements
Must have
• simple look and design. Unique design
Nice to have
• I attached the 2 logo separate from the main logo. This can be used separately from the Main Logo, together with the main logo or as main logo. I included the logo font. Use it or not, designers choice.
Should not have
• cookie cutter design. Little use of red other than the logo

```html
<!DOCTYPE html>
<html lang="en">
<head>
<meta charset="utf-8">
<title>Roam4ward Business Card</title>
<link rel="stylesheet" href="https://fonts.googleapis.com/css2?family=Montserrat:wght@400;500;700&display=swap">
<style>
  :root {
    --stage: #2b2b2b;
    --card-black: #050505;
    --brand-red: #ec1c24;
    --ink-white: #ffffff;
    --ink-soft: #e8e8e8;
  }
  * { margin: 0; padding: 0; box-sizing: border-box; }
  html, body {
    width: 1200px; height: 900px; overflow: hidden;
    background: var(--stage);
    font-family: "Montserrat", sans-serif;
  }
  .stage {
    width: 1200px; height: 900px;
    display: flex; flex-direction: column;
    align-items: center; justify-content: center; gap: 56px;
  }
  .card {
    position: relative;
    width: 640px; height: 366px;
    background: var(--card-black);
    border-radius: 18px;
    overflow: hidden;
    box-shadow: 0 14px 30px rgba(0,0,0,0.45);
  }
  /* Front */
  .card-front .brand-mark {
    position: absolute; left: 0; right: 0; top: 120px;
    display: flex; align-items: center; justify-content: center; gap: 14px;
  }
  .brand-dot {
    width: 34px; height: 34px; border-radius: 50%;
    background: var(--brand-red);
  }
  .brand-name {
    color: var(--ink-white);
    font-weight: 700;
    font-size: 52px;
    letter-spacing: -0.5px;
  }
  .card-front .front-web {
    position: absolute; left: 0; right: 0; bottom: 66px;
    text-align: center;
    color: var(--ink-white);
    font-size: 17px; font-weight: 500;
    letter-spacing: 0.5px;
  }
  .front-web .web-accent { color: var(--brand-red); }
  /* Back */
  .card-back .side-band {
    position: absolute; left: 0; top: 0; bottom: 0;
    width: 62px; background: var(--brand-red);
  }
  .card-back .back-brand {
    position: absolute; right: 44px; top: 48px;
    display: flex; align-items: center; gap: 10px;
  }
  .back-brand .brand-name { font-size: 34px; }
  .back-brand .brand-dot { width: 22px; height: 22px; }
  .contact-block {
    position: absolute; left: 96px; top: 150px;
    color: var(--ink-soft);
  }
  .person-name {
    color: var(--brand-red);
    font-weight: 700; font-size: 24px; line-height: 1.1;
  }
  .person-title { font-size: 15px; margin-bottom: 14px; }
  .address-line { font-size: 15px; line-height: 1.4; }
  .contact-list { list-style: none; margin-top: 14px; }
  .contact-list li {
    display: flex; align-items: center; gap: 10px;
    font-size: 15px; line-height: 1.55;
  }
  .contact-list svg { width: 14px; height: 14px; flex: none; }
  .contact-list strong { font-weight: 700; color: var(--ink-white); }
</style>
</head>
<body>
<main class="stage">
  <section class="card card-front">
    <div class="brand-mark">
      <span class="brand-dot"></span>
      <span class="brand-name">roam4ward</span>
    </div>
    <p class="front-web">www.<span class="web-accent">roam4ward</span>.example</p>
  </section>

  <section class="card card-back">
    <div class="side-band"></div>
    <div class="back-brand">
      <span class="brand-dot"></span>
      <span class="brand-name">roam4ward</span>
    </div>
    <div class="contact-block">
      <h1 class="person-name">Marco T Villena</h1>
      <p class="person-title">President/CEO</p>
      <p class="address-line">4127 Brindle Oak Way #164</p>
      <p class="address-line">Orlando, FL 32899</p>
      <ul class="contact-list">
        <li>
          <svg viewBox="0 0 16 16" aria-hidden="true"><circle cx="8" cy="8" r="8" fill="#ec1c24"/><path d="M5 4.5l1.6-.5 1 2-1 .8c.5 1 1.2 1.7 2.2 2.2l.8-1 2 1-.5 1.6c-3.2.2-6.3-2.9-6.1-6.1z" fill="#050505"/></svg>
          (407) 555-0182
        </li>
        <li>
          <svg viewBox="0 0 16 16" aria-hidden="true"><circle cx="8" cy="8" r="8" fill="#ec1c24"/><rect x="4" y="5" width="8" height="6" fill="none" stroke="#050505" stroke-width="1.2"/><path d="M4 5l4 3.2L12 5" fill="none" stroke="#050505" stroke-width="1.2"/></svg>
          mvillena@roam4ward.example
        </li>
        <li>
          <svg viewBox="0 0 16 16" aria-hidden="true"><circle cx="8" cy="8" r="8" fill="#ec1c24"/><circle cx="8" cy="8" r="4" fill="none" stroke="#050505" stroke-width="1.1"/><path d="M4 8h8M8 4c-2 2.5-2 5.5 0 8M8 4c2 2.5 2 5.5 0 8" fill="none" stroke="#050505" stroke-width="1"/></svg>
          <span>www.<strong>roam4ward</strong>.example</span>
        </li>
      </ul>
    </div>
  </section>
</main>
</body>
</html>
```